Business Card Design

I have been a licensed, bonded and insured electrical contractor for 30+ years, working primarily in The Villages, Spruce Creek and surrounding areas of Central Florida. I also maintain Master Beacon Fellow designation from the National Fixture Guild. They do have a logo that we are able to use. I am an expert trouble shooting person and install primarily LED under cabinet lighting, flat screen televisions and recessed lighting. Services are very affordable. Pinecrest Electrical Service is not the company name.
Updates

Thank you for all of the great submissions. I do have one in mind so far. L.E.D.'s are different from the lamps shown on all of the cards. Shown is an incandescent or compact fluorescent lamp. Both will be obsolete before long. Please include my e-mail address hmarlo@quillpost.net on the card. This is not for your personal use. Thank you again.

I am still waiting for someone to get rid of the CFL lamps on the card and show me an LED. What's up?

Industry/Entity Type

Electrical

Contact Information for Business Card

Harold Marlo, Pinecrest Electrical Sevice, Electrical License #QR58419362, 352-555-0187, National Fixture Guild Master Beacon Fellow, 30 years Experience,

Requirements
Nice to have
• I do not have the NFG logo but would like to on the card along with something indicating electrical work.

```html
<!DOCTYPE html>
<html lang="en">
<head>
<meta charset="utf-8">
<title>Harold Marlo — Business Card</title>
<link rel="stylesheet" href="https://fonts.googleapis.com/css2?family=Noto+Sans:wght@400;700&display=swap">
<style>
  :root {
    --stage: #e9e6e1;
    --card-black: #0a0a0a;
    --card-edge: #1c1c1c;
    --text-white: #f4f4f4;
    --name-cream: #f3e6d6;
    --accent-orange: #e8902e;
    --night-blue: #0f2a44;
    --pool-blue: #2a7fa8;
    --lamp-amber: #c98a3a;
  }
  * { box-sizing: border-box; margin: 0; padding: 0; }
  html, body {
    width: 1200px; height: 891px; overflow: hidden;
    background: var(--stage);
    font-family: "Noto Sans", Verdana, sans-serif;
  }
  .canvas {
    position: relative; width: 1200px; height: 891px;
    display: flex; flex-direction: column; align-items: center; justify-content: center; gap: 44px;
  }
  .card {
    position: relative; width: 600px; height: 343px;
    border-radius: 22px; overflow: hidden;
    background: var(--card-black);
    box-shadow: 0 10px 26px rgba(0,0,0,.35);
    color: var(--text-white);
  }
  /* Front card */
  .card--front {
    background: radial-gradient(ellipse at 55% 30%, #2a2a2a 0%, var(--card-black) 60%);
    display: flex; flex-direction: column; align-items: center; justify-content: center;
    text-align: center; padding: 0 30px;
  }
  .brand { display: flex; align-items: center; gap: 12px; }
  .brand__dot { width: 20px; height: 20px; border-radius: 50%; background: var(--name-cream); }
  .brand__name { font-weight: 700; font-size: 40px; color: var(--name-cream); letter-spacing: .5px; }
  .front__guild { margin-top: 14px; font-size: 15px; font-weight: 700; }
  .front__years { font-size: 19px; font-weight: 700; margin-top: 2px; }
  .front__specialty { margin-top: 44px; font-size: 21px; font-weight: 700; letter-spacing: .5px; }

  /* Back card */
  .card__scene {
    position: absolute; left: 0; top: 56px; width: 100%; height: 287px;
    background:
      radial-gradient(ellipse at 22% 60%, rgba(201,138,58,.75) 0%, rgba(201,138,58,0) 38%),
      radial-gradient(ellipse at 78% 30%, rgba(42,127,168,.8) 0%, rgba(42,127,168,0) 45%),
      linear-gradient(180deg, var(--card-black) 0%, var(--night-blue) 45%, #0b1620 100%);
  }
  .card--back .brand { position: absolute; left: 150px; top: 22px; }
  .card--back .brand__name { font-size: 34px; }
  .back__service {
    position: absolute; left: 176px; top: 74px;
    font-size: 17px; font-weight: 700; color: var(--name-cream);
  }
  .contact {
    position: absolute; right: 36px; top: 150px;
    list-style: none; text-align: right; font-weight: 700; line-height: 1.2;
    text-shadow: 0 1px 3px rgba(0,0,0,.8);
  }
  .contact__row { font-size: 16px; }
  .contact__row--phone { font-size: 22px; }
  .contact__label { color: var(--accent-orange); }
  .contact__value { color: var(--text-white); }
  .back__guild {
    position: absolute; left: 0; right: 0; bottom: 18px; text-align: center;
    font-size: 15px; font-weight: 700; text-shadow: 0 1px 3px rgba(0,0,0,.8);
  }
</style>
</head>
<body>
<main class="canvas">
  <section class="card card--front">
    <div class="brand">
      <span class="brand__dot"></span>
      <span class="brand__name">Harold Marlo</span>
    </div>
    <p class="front__guild">National Fixture Guild Master Beacon Fellow</p>
    <p class="front__years">30 years experience</p>
    <p class="front__specialty">Specialty: Undercabinet LED Lighting</p>
  </section>

  <section class="card card--back">
    <div class="card__scene" role="img" aria-label="Night photograph of a home and pool lit by landscape lighting"></div>
    <div class="brand">
      <span class="brand__dot"></span>
      <span class="brand__name">Harold Marlo</span>
    </div>
    <p class="back__service">Pinecrest Electrical Sevice</p>
    <ul class="contact">
      <li class="contact__row contact__row--phone"><span class="contact__label">Mobile:</span> <span class="contact__value">352-555-0187</span></li>
      <li class="contact__row"><span class="contact__label">E-mail:</span> <span class="contact__value">hmarlo@quillpost.net</span></li>
      <li class="contact__row"><span class="contact__label">Electrical License:</span> <span class="contact__value">#QR58419362</span></li>
      <li class="contact__row"><span class="contact__label">Experience:</span> <span class="contact__value">30 years</span></li>
    </ul>
    <p class="back__guild">National Fixture Guild Master Beacon Fellow</p>
  </section>
</main>
</body>
</html>
```